Odvetnik - Attorney at law
Sodni tolmač za angleški jezik - English language Court Interpreter
Simple
Marjan Lesk
Odvetnik - Attorney at law Sodni tolmač za angleški jezik - English Language Court Interpreter
Brinjeva ulica 41 6000 Koper Slovenija
info@marjanlesk.example
www.marjanlesk.example
I invite all designers under logo project Attorney Marjan Lesk to participate. Please inform all designers.

```html
<!DOCTYPE html>
<html lang="sl">
<head>
<meta charset="utf-8">
<title>Marjan Lesk – Business Card</title>
<link rel="stylesheet" href="https://fonts.googleapis.com/css2?family=Marcellus&family=Open+Sans:wght@400;700&display=swap">
<style>
  :root {
    --backdrop: #3a3a3a;
    --paper: #ffffff;
    --indigo: #3d3a7c;
    --orange: #ef7d2c;
    --ink: #1c1c1c;
  }
  html, body {
    margin: 0;
    width: 1200px;
    height: 745px;
    overflow: hidden;
    background: var(--backdrop);
  }
  .card {
    position: absolute;
    left: 226px;
    top: 158px;
    width: 746px;
    height: 427px;
    background: var(--paper);
    font-family: "Open Sans", Arial, sans-serif;
    color: var(--ink);
    overflow: hidden;
  }
  .band { position: absolute; left: 0; right: 0; }
  .band--top-indigo { top: 0; height: 22px; background: var(--indigo); }
  .band--top-orange { top: 25px; height: 5px; background: var(--orange); }
  .band--bottom-orange { top: 392px; height: 5px; background: var(--orange); }
  .band--bottom-indigo { top: 400px; bottom: 0; background: var(--indigo); }

  .brand__dot {
    position: absolute;
    left: 112px;
    top: 100px;
    width: 64px;
    height: 64px;
    border-radius: 50%;
    background: var(--orange);
  }
  .brand__name {
    position: absolute;
    left: 212px;
    top: 86px;
    font-family: "Marcellus", "Times New Roman", serif;
    font-size: 64px;
    line-height: 1;
    letter-spacing: 0.5px;
    color: var(--indigo);
    white-space: nowrap;
  }
  .brand__tagline {
    position: absolute;
    left: 206px;
    top: 150px;
    font-family: "Marcellus", "Times New Roman", serif;
    font-size: 29px;
    line-height: 1.2;
    color: var(--indigo);
    white-space: nowrap;
  }

  .details__text {
    position: absolute;
    left: 0;
    right: 0;
    margin: 0;
    text-align: center;
    white-space: nowrap;
    line-height: 1;
    font-size: 17px;
  }
  .details__name { top: 220px; font-weight: 700; font-size: 20px; }
  .details__role { top: 254px; font-size: 14.5px; }
  .details__address { top: 310px; }
  .details__web { top: 334px; }
  .details__phone { top: 358px; }
  .details__label { font-weight: 700; }
</style>
</head>
<body>
  <div class="card">
    <div class="band band--top-indigo"></div>
    <div class="band band--top-orange"></div>

    <div class="brand__dot"></div>
    <span class="brand__name">MARJAN LESK</span>
    <span class="brand__tagline">Odvetnik - Attorney at law</span>

    <p class="details__text details__name">Marjan Lesk</p>
    <p class="details__text details__role">Odvetnik - Attorney at law Sodni tolmač za angleški jezik - English Language Court Interpreter</p>
    <p class="details__text details__address"><span class="details__label">A:</span> Brinjeva ulica 41 6000 Koper Slovenija</p>
    <p class="details__text details__web"><span class="details__label">E:</span> info@marjanlesk.example | <span class="details__label">W:</span> www.marjanlesk.example</p>
    <p class="details__text details__phone"><span class="details__label">P:</span> +386 5 6104520 | <span class="details__label">C:</span> +386 41555018 | <span class="details__label">F:</span> +386 5 6104521</p>

    <div class="band band--bottom-orange"></div>
    <div class="band band--bottom-indigo"></div>
  </div>
</body>
</html>
```